Simple and clean

We need a business card design for a new company called Dwelling Owl. It is a search engine to find current properties for sale or rent in New Zealand market.
We have already a colour scheme that we would like people to use.
Light brown: #D4CCB0
Light green: #D6E4D4
Green: #669966
Black/White
It is OK to divert from this colour scheme slightly as long as there is a green component to the business card.
Final design should be clean, simple and should communicate the nature of the business.
Target Market(s)
- First home buyers
- Real estate agents
- People seeking rentals
Industry/Entity Type
Business
Requirements
Must have
- Use those or similar colours.
Light brown: #D4CCB0
Light green: #D6E4D4
Green: #669966
Black/White

```html
<!DOCTYPE html>
<html lang="en">
<head>
<meta charset="UTF-8">
<title>Dwelling Owl – Business Card</title>
<link href="https://fonts.googleapis.com/css2?family=Rokkitt:wght@400;600;700&display=swap" rel="stylesheet">
<style>
  :root {
    --green-deep: #1f6b1f;
    --green-mid: #3f9a35;
    --green-light: #6cc05e;
    --band-beige: rgba(222, 218, 190, 0.93);
    --panel-mint: #d6ecd0;
    --ink-dark: #3b3b3b;
    --ink-green: #2f6e2a;
    --white: #ffffff;
  }
  * { margin: 0; padding: 0; box-sizing: border-box; }
  html, body {
    width: 1200px; height: 686px; overflow: hidden;
    background: #f2f2f2;
  }
  .card {
    position: relative;
    width: 1200px; height: 686px;
    overflow: hidden;
    font-family: "Rokkitt", serif;
    background: linear-gradient(160deg, var(--green-mid) 0%, #358a2c 45%, var(--green-deep) 100%);
  }
  .backdrop-glow {
    position: absolute; inset: 0;
    background:
      radial-gradient(ellipse 720px 300px at 72% 16%, rgba(140,210,120,0.55) 0%, rgba(140,210,120,0) 70%),
      radial-gradient(ellipse 500px 260px at 88% 42%, rgba(120,200,100,0.35) 0%, rgba(120,200,100,0) 70%);
  }
  .divider {
    position: absolute; left: 703px; top: 0;
    width: 2px; height: 686px;
    background: rgba(255,255,255,0.18);
  }
  .web-line {
    position: absolute; top: 72px; left: 0; width: 100%;
    text-align: center; color: var(--white);
    font-size: 34px; letter-spacing: 0.5px;
  }
  .brand-band {
    position: absolute; left: 0; top: 145px;
    width: 703px; height: 167px;
    background: var(--band-beige);
  }
  .brand-mark {
    position: absolute; left: 23px; top: 141px;
    width: 178px; height: 178px; border-radius: 50%;
    background: var(--white);
  }
  .brand-name {
    position: absolute; left: 222px; top: 186px;
    font-size: 68px; font-weight: 700;
    color: var(--ink-dark); line-height: 1;
  }
  .person-panel {
    position: absolute; left: 480px; top: 398px;
    width: 720px; height: 146px;
    background: var(--panel-mint);
  }
  .person-name {
    position: absolute; left: 851px; top: 414px;
    font-size: 48px; font-weight: 400;
    color: var(--ink-dark); line-height: 1;
  }
  .person-role {
    position: absolute; left: 851px; top: 464px;
    font-size: 36px; font-weight: 700;
    color: var(--ink-green); line-height: 1;
  }
  .address, .phones {
    position: absolute; top: 594px;
    color: var(--white); font-size: 30px; line-height: 40px;
  }
  .address { left: 32px; }
  .phones { right: 30px; text-align: right; }
</style>
</head>
<body>
  <div class="card">
    <div class="backdrop-glow" role="img" aria-label="Soft light green swirl backdrop"></div>

    <div class="divider"></div>

    <p class="web-line">info@dwellingowl.co.nz | www.dwellingowl.co.nz</p>

    <div class="brand-band"></div>
    <div class="brand-mark"></div>
    <div class="brand-name">Dwelling Owl</div>

    <div class="person-panel"></div>
    <div class="person-name">Mara Quinlan</div>
    <div class="person-role">Developer</div>

    <div class="address">
      <div>14 Kauri Lane Auckland</div>
      <div>PO.BOX.48215</div>
    </div>
    <div class="phones">
      <div>+30 41873052</div>
      <div>+30 41873053</div>
    </div>
  </div>
</body>
</html>
```